2013 Golf Outing Flyer

Our charitable organization was created in honor of my daughter who died at age 16. Our annual fundraiser is a golf tournament. I am not a creative person so I'd like someone to design a printable flyer that grabs people's attention but is not too busy while incorportating our organization's logo with the basic information.

Event details:
3rd Annual Marisol Quinn Dorsey Memorial Golf Tournament
4 person scramble

Saturday October 5th, 2013
Fernhollow Golf Club, Auburn, IL
9:30 Registration
Shotgun start at noon
To Register go online to www.marisolqdorseygolf.teeupsignups.example or email
marisoldorseyscholarship@mailbox.example

Scholarships to Cedar Ridge High School seniors are made possible by our orgnization through this fundraiser.
Updates

Target Market(s)

golfers and businesses willing to sponsor event

Industry/Entity Type

School

Requirements
Must have
• single page-easy to print
includes non profit organization logo which I attached (think I did)
Specific information about the tournament- date and location and registration info
Nice to have
• company logo and the golf outing logo but if both are too much, then just the golf logo and the organization name can be at the bottom

```html
<!DOCTYPE html>
<html lang="en">
<head>
<meta charset="utf-8">
<title>3rd Annual Marisol Quinn Dorsey Memorial Golf Tournament</title>
<link rel="stylesheet" href="https://fonts.googleapis.com/css2?family=Alegreya:wght@400;500&family=Tinos:wght@400;700&display=swap">
<style>
  :root {
    --page-bg: #efeae4;
    --frame: #111111;
    --navy: #1c3f8c;
    --green: #3a9a3e;
    --band-top: #1b8fdc;
    --band-bottom: #1b4e9e;
    --sky: #a9cde6;
    --grass-light: #7fb04a;
    --grass-dark: #2f5a1c;
    --white: #ffffff;
    --ink: #1a1a1a;
    --button-top: #3f7fc4;
    --button-bottom: #123f7d;
  }
  * { box-sizing: border-box; margin: 0; padding: 0; }
  html, body { width: 1200px; height: 900px; overflow: hidden; }
  body {
    background: var(--page-bg);
    display: flex;
    align-items: center;
    justify-content: center;
  }
  .flyer {
    width: 600px;
    height: 840px;
    border: 7px solid var(--frame);
    background: var(--white);
    display: flex;
    flex-direction: column;
  }
  .hero {
    position: relative;
    height: 415px;
    overflow: hidden;
  }
  .hero-photo {
    position: absolute;
    inset: 0;
    background: linear-gradient(180deg, var(--sky) 0%, #c8dcc0 28%, var(--grass-light) 55%, var(--grass-dark) 100%);
  }
  .edition-badge {
    position: absolute;
    inset: 0;
  }
  .edition-text {
    position: absolute;
    left: 347px;
    top: 22px;
    font-family: "Tinos", serif;
    color: var(--navy);
    display: flex;
    align-items: flex-start;
  }
  .edition-number {
    font-size: 132px;
    font-weight: 700;
    line-height: 0.9;
    letter-spacing: -4px;
  }
  .edition-suffix {
    display: flex;
    flex-direction: column;
    margin-left: 2px;
    margin-top: 12px;
  }
  .edition-ordinal {
    font-size: 50px;
    font-weight: 700;
    color: var(--green);
    line-height: 1;
  }
  .edition-word {
    font-size: 33px;
    line-height: 1;
    margin-top: 6px;
    padding-bottom: 3px;
    border-bottom: 2px solid var(--navy);
  }
  .details {
    height: 303px;
    background: linear-gradient(180deg, var(--band-top) 0%, #1a6cc0 50%, var(--band-bottom) 100%);
    color: var(--white);
    font-family: "Alegreya", serif;
    text-align: center;
    padding-top: 14px;
  }
  .event-title {
    font-size: 36px;
    font-weight: 400;
    line-height: 1.22;
  }
  .event-format {
    font-size: 36px;
    line-height: 1.1;
    margin-top: 4px;
  }
  .event-info {
    list-style: none;
    font-size: 22px;
    line-height: 1.45;
  }
  .event-info li:nth-child(2) { margin-bottom: 4px; }
  .registration {
    flex: 1;
    display: flex;
    align-items: center;
    padding: 0 10px;
    gap: 18px;
  }
  .register-button {
    width: 124px;
    height: 66px;
    border-radius: 8px;
    background: linear-gradient(180deg, var(--button-top) 0%, var(--button-bottom) 100%);
    border: 2px solid #0d2c5a;
    color: var(--white);
    font-family: "Tinos", serif;
    font-weight: 700;
    font-size: 22px;
    line-height: 1.05;
    text-align: center;
    display: flex;
    align-items: center;
    justify-content: center;
  }
  .contact {
    font-family: "Tinos", serif;
    color: var(--ink);
    font-size: 17px;
    line-height: 1.75;
    text-align: center;
    flex: 1;
  }
</style>
</head>
<body>
  <main class="flyer">
    <section class="hero">
      <div class="hero-photo" role="img" aria-label="Photo of a gloved hand placing a golf ball on a red tee beside an iron club on the fairway"></div>
      <svg class="edition-badge" width="586" height="415" viewBox="0 0 586 415" aria-hidden="true">
        <circle cx="516" cy="-7" r="262" fill="var(--navy)"/>
        <circle cx="516" cy="-7" r="252" fill="var(--white)"/>
        <circle cx="508" cy="-14" r="246" fill="var(--green)"/>
        <circle cx="508" cy="-14" r="238" fill="var(--white)"/>
      </svg>
      <div class="edition-text">
        <span class="edition-number">3</span>
        <span class="edition-suffix">
          <span class="edition-ordinal">RD</span>
          <span class="edition-word">ANNUAL</span>
        </span>
      </div>
    </section>
    <section class="details">
      <h1 class="event-title">Marisol Quinn Dorsey<br>Memorial Golf Tournament</h1>
      <p class="event-format">4 person scramble</p>
      <ul class="event-info">
        <li>9:30 Registration</li>
        <li>Shotgun start at noon</li>
        <li>Saturday October 5th, 2013</li>
        <li>Fernhollow Golf Club, Auburn, IL</li>
      </ul>
    </section>
    <footer class="registration">
      <div class="register-button">Register<br>Now</div>
      <div class="contact">
        <p>www.marisolqdorseygolf.teeupsignups.example</p>
        <p>marisoldorseyscholarship@mailbox.example</p>
      </div>
    </footer>
  </main>
</body>
</html>
```